Letterbox promotional card

Boutique real estate agency needs postcard (no address/stamp space) to promote business via letterboxing, café distribution, etc.
Needs contact details as per attached business card, clean look, company colours, logo and catch phrase as per the T-shirt design attached.
Do not include 'Sales' from the business card. Add another name and mobile number-
Berin Calloway 0468 193 742

Target Market(s)

Potential property vendors.

Industry/Entity Type

Real Estate

Requirements
Must have
• REVISEDText for reverse side of card: Use dot points, one per line - (no dot point for the Considering selling?)-
• Considering selling?
• No obligation appraisal
• Integrity
• Personalised service
• Individualised marketing programs
• Quality
Nice to have
• Considering selling?
• No obligation appraisal
• Integrity
• Personalised service
Should not have
• Property photos; too much text

```html
<!DOCTYPE html>
<html lang="en">
<head>
<meta charset="utf-8">
<title>Harlow Brennan Real Estate – Letterbox Card</title>
<link href="https://fonts.googleapis.com/css2?family=PT+Sans:wght@400;700&family=PT+Sans+Narrow:wght@400;700&display=swap" rel="stylesheet">
<style>
  :root {
    --backdrop: #d8c4a0;
    --navy: #123a52;
    --gold: #8e7a28;
    --gold-text: #8c6a1e;
    --paper: #ffffff;
    --band-light: #e3dacb;
    --band-mid: #cbb898;
    --photo-grey: #8f8f8c;
    --photo-dark: #3d3b46;
  }
  * { margin: 0; padding: 0; box-sizing: border-box; }
  html, body { width: 1200px; height: 500px; overflow: hidden; }
  body {
    position: relative;
    background: var(--backdrop);
    font-family: "PT Sans Narrow", "Arial Narrow", sans-serif;
    color: var(--navy);
  }
  .card {
    position: absolute;
    background: var(--paper);
    border: 6px solid var(--gold);
    overflow: hidden;
  }
  .card--front { left: 28px; top: 35px; width: 560px; height: 434px; }
  .card--back { left: 615px; top: 35px; width: 558px; height: 434px; }

  .abs { position: absolute; }

  /* front */
  .front-shape { left: 0; top: 0; }
  .photo { background: linear-gradient(160deg, var(--photo-grey), var(--photo-dark)); }
  .photo--agent-one { left: 26px; top: 11px; width: 154px; height: 215px; }
  .photo--agent-two { left: 371px; top: 197px; width: 98px; height: 122px;
    background: linear-gradient(160deg, #9c9a96, #3b3a3f); }

  .agent-name {
    font-family: "PT Sans", sans-serif;
    font-weight: 700;
    color: var(--gold-text);
    font-size: 16px;
    letter-spacing: 2px;
  }
  .agent-line { font-size: 14.5px; color: #1d2a33; }

  .details { left: 28px; top: 288px; font-size: 14.5px; line-height: 17px; color: #1d2a33; }
  .details td { padding: 0; }
  .details td:first-child { width: 40px; }

  .front-footer {
    left: 0; bottom: 0; width: 100%; height: 51px;
    background: var(--navy);
    color: #b59a4e;
    font-size: 13px;
    text-align: center;
    padding-top: 7px;
    line-height: 15px;
  }

  .brand {
    font-family: "PT Sans", sans-serif;
    font-weight: 700;
    color: var(--navy);
    text-align: center;
    line-height: 1;
  }
  .brand__top { display: block; letter-spacing: 1px; }
  .brand__bottom { display: block; letter-spacing: 2px; }

  .brand--front { left: 330px; top: 18px; width: 180px; }
  .brand--front .brand__top { font-size: 27px; }
  .brand--front .brand__bottom { font-size: 19px; margin-top: 6px; }

  .town { font-family: "PT Sans", sans-serif; color: var(--navy); text-align: center; }
  .tagline { font-family: "PT Sans", sans-serif; font-weight: 700; color: var(--gold-text); text-align: center; }
  .site { font-family: "PT Sans", sans-serif; font-weight: 700; color: var(--navy); text-align: center; }

  .front-block { left: 314px; width: 212px; }

  /* back */
  .brand--back { left: 40px; top: 80px; width: 210px; }
  .brand--back .brand__top { font-size: 31px; }
  .brand--back .brand__bottom { font-size: 22px; margin-top: 8px; }
  .back-block { left: 20px; width: 250px; }

  .rule { height: 3px; background: var(--gold); }
  .pitch {
    left: 305px; top: 126px; width: 215px;
    font-size: 15.5px; line-height: 21.5px;
    color: var(--gold-text);
  }
  .back-contact { left: 20px; width: 250px; text-align: center; font-size: 14px; color: #1d2a33; }
  .back-contact .phone { font-size: 16px; display: inline-flex; align-items: center; gap: 8px; }

  .back-band {
    left: 0; top: 367px; width: 100%; height: 55px;
    background: var(--band-light);
  }
  .back-band__center {
    position: absolute; left: 116px; top: 0; width: 318px; height: 100%;
    background: var(--band-mid);
    color: var(--gold-text);
    font-family: "PT Sans", sans-serif; font-weight: 700;
    font-size: 15px; letter-spacing: 2px;
    display: flex; align-items: center; justify-content: center;
  }
</style>
</head>
<body>

<section class="card card--front">
  <svg class="abs front-shape" width="548" height="422" viewBox="0 0 548 422" aria-hidden="true">
    <polygon points="278,0 292,0 292,375 278,375" fill="#8e7a28"/>
    <polygon points="246,0 282,0 282,375 246,375 262,292 262,86" fill="#123a52"/>
    <polygon points="282,0 298,0 282,86 282,292 298,375 282,375" fill="#8e7a28"/>
  </svg>

  <div class="abs photo photo--agent-one" role="img" aria-label="Portrait photo of Marla Fenwick seated with her dog"></div>
  <div class="abs agent-name" style="left:28px;top:240px;">Marla Fenwick</div>
  <div class="abs agent-line" style="left:28px;top:259px;">mobile&nbsp;&nbsp;&nbsp;0468.193.742</div>

  <table class="abs details">
    <tr><td colspan="2">52 Kessel St., Goulburn NSW 2580</td></tr>
    <tr><td style="height:4px"></td><td></td></tr>
    <tr><td>ph</td><td>&nbsp;&nbsp;&nbsp;&nbsp;&nbsp;&nbsp;02.4830.1157</td></tr>
    <tr><td>fax</td><td>&nbsp;&nbsp;&nbsp;&nbsp;&nbsp;&nbsp;02.4830.1158</td></tr>
    <tr><td>email</td><td>&nbsp;info@harlowbrennan.com</td></tr>
  </table>

  <div class="abs brand brand--front">
    <span class="brand__top">HARLOW BRENNAN</span>
    <span class="brand__bottom">REAL ESTATE</span>
  </div>
  <div class="abs front-block town" style="top:112px;font-size:19px;">Goulburn</div>
  <div class="abs front-block tagline" style="top:137px;font-size:19px;">Making a difference</div>
  <div class="abs front-block site" style="top:163px;font-size:15px;">www.harlowbrennan.com</div>

  <div class="abs photo photo--agent-two" role="img" aria-label="Portrait photo of Berin Calloway"></div>
  <div class="abs agent-name" style="left:346px;top:327px;width:150px;text-align:center;">Berin Calloway</div>
  <div class="abs agent-line" style="left:346px;top:346px;width:150px;text-align:center;">mobile&nbsp;&nbsp;&nbsp;0468.193.742</div>

  <div class="abs front-footer">
    Real Estate and Stock And Station Agent Number 3308152<br>
    ABN 61 408 223 517
  </div>
</section>

<section class="card card--back">
  <div class="abs brand brand--back">
    <span class="brand__top">HARLOW BRENNAN</span>
    <span class="brand__bottom">REAL ESTATE</span>
  </div>
  <div class="abs back-block town" style="top:190px;font-size:22px;">Goulburn</div>
  <div class="abs back-block tagline" style="top:219px;font-size:22px;">Making a difference</div>
  <div class="abs back-block site" style="top:249px;font-size:16.5px;">www.harlowbrennan.com</div>

  <div class="abs back-contact" style="top:309px;">52 Kessel St, Goulburn NSW 2580</div>
  <div class="abs back-contact" style="top:328px;">
    <span class="phone">
      <svg width="12" height="14" viewBox="0 0 12 14" aria-hidden="true">
        <path d="M3 1 L5 4 L3.6 5.4 C4.4 7.4 5.6 8.6 7.4 9.6 L8.8 8.2 L11 10.4 L9 12.6 C5 12 1.4 8 1 3.2 Z" fill="none" stroke="#123a52" stroke-width="1.2"/>
      </svg>
      0451 276 804
    </span>
  </div>

  <div class="abs rule" style="left:305px;top:76px;width:202px;"></div>
  <p class="abs pitch">
    If you are considering selling, please contact us for a free, no obligation appraisal of your property.<br>
    Our business is built on integrity.<br>
    We offer personalised service and individual marketing programs for all listed properties.
  </p>
  <div class="abs rule" style="left:305px;top:309px;width:202px;"></div>

  <div class="abs back-band">
    <div class="back-band__center">www.harlowbrennan.com</div>
  </div>
</section>

</body>
</html>
```